Website redesign

Redesign the Website

http://www.lindmark-schoefer.de/

Task

- make 1 Layout for the Website
- Colors: white, yellow, brown
- Text: Take from Page - ore rather Use Latin - Lore Ipsum ...
- pimp design and overall look
- enhance overview for better orientation
- more freindly / sympatic overall look.
- Better integrate Mingleroo Button aso.
- send Layout as layered PSD

```html
<!DOCTYPE html>
<html lang="de">
<head>
<meta charset="utf-8">
<title>Lindmark Schöfer – Trauringe</title>
<link rel="stylesheet" href="https://fonts.googleapis.com/css2?family=Libre+Baskerville&family=Montserrat:wght@400;600;700&family=Open+Sans:wght@300;400;600&display=swap">
<style>
:root{
  --yellow:#e9b503;
  --yellow-dark:#c99a00;
  --brown:#3b2417;
  --brown-deep:#2a180f;
  --grey-band:#ececec;
  --ink:#333;
  --muted:#777;
  --dark:#1f1f1f;
  --darker:#151515;
  --white:#fff;
}
*{box-sizing:border-box;margin:0;padding:0}
html,body{width:1200px;height:2784px;overflow:hidden;background:var(--white)}
body{font-family:"Open Sans",sans-serif;color:var(--ink);position:relative}
.btn{display:inline-block;font-family:"Montserrat",sans-serif;font-size:12px;font-weight:600;letter-spacing:.5px;text-transform:uppercase;padding:11px 20px;border-radius:2px}
.btn-yellow{background:var(--yellow);color:var(--brown)}
.btn-brown{background:var(--brown);color:var(--white)}

/* header */
.site-header{height:100px;display:flex;align-items:center;justify-content:space-between;padding:0 48px}
.brand{display:flex;align-items:center;gap:10px;font-family:"Montserrat",sans-serif;font-weight:700;font-size:20px;color:var(--yellow-dark)}
.brand-dot{width:26px;height:26px;border-radius:50%;background:var(--yellow)}
.contact-bar{display:flex;gap:40px;font-size:14px;color:var(--ink)}
.contact-bar span{display:flex;align-items:center;gap:10px}
.icon-round{width:30px;height:30px;border-radius:50%;background:var(--yellow);display:flex;align-items:center;justify-content:center}

/* nav */
.main-nav{height:52px;background:var(--yellow);display:flex;align-items:center;padding:0 48px;gap:4px}
.main-nav a{font-family:"Montserrat",sans-serif;font-size:14px;color:var(--brown);padding:10px 26px;text-decoration:none}
.main-nav a.active{background:var(--yellow-dark);color:var(--white);border-radius:3px}

/* hero */
.hero{height:648px;background:linear-gradient(90deg,var(--brown-deep),var(--brown) 60%,#4a2e1d);position:relative;overflow:hidden}
.hero-text{position:absolute;left:48px;top:220px;width:520px;color:var(--white)}
.hero-text h1{font-family:"Libre Baskerville",serif;font-weight:400;font-size:50px;line-height:60px;margin-bottom:28px}
.hero-text p{font-size:14px;line-height:22px;color:#e6dcd4;margin-bottom:26px}
.hero-visual{position:absolute;right:40px;top:50px;width:560px;height:500px;border-radius:50%;background:radial-gradient(circle at 50% 50%,#f6d56a,#c89624 45%,rgba(59,36,23,0) 72%)}
.hero-dots{position:absolute;bottom:70px;left:50%;transform:translateX(-50%);display:flex;gap:8px}
.hero-dots i{width:9px;height:9px;border-radius:50%;background:#8a7566}
.hero-dots i.on{background:var(--white)}

/* welcome */
.welcome{height:320px;text-align:center;padding-top:50px}
.section-title{display:flex;align-items:center;justify-content:center;gap:26px;font-family:"Montserrat",sans-serif;font-weight:700;font-size:36px;color:var(--brown)}
.section-title::before,.section-title::after{content:"";width:270px;height:1px;background:#cfcfcf}
.section-title em{font-style:normal;color:var(--yellow)}
.welcome p{width:1000px;margin:30px auto 26px;font-size:13px;line-height:22px;color:var(--muted)}

/* feature band */
.feature{height:440px;background:var(--grey-band);position:relative}
.feature-text{position:absolute;left:48px;top:72px;width:700px}
.feature-text h2{font-family:"Open Sans",sans-serif;font-weight:400;font-size:44px;line-height:56px;color:var(--ink);margin-bottom:24px}
.feature-text p{font-size:13px;line-height:22px;color:var(--muted);margin-bottom:22px}
.feature-visual{position:absolute;right:0;top:0;width:440px;height:440px;background:linear-gradient(135deg,#e7c9b3,#b78a6d 55%,#5a3828)}

/* services */
.services{height:600px;padding-top:80px}
.service-grid{display:flex;gap:36px;padding:0 48px;margin-top:40px}
.service-card{width:252px;text-align:center}
.service-visual{height:240px;background:linear-gradient(180deg,#f4f4f4,#e2e2e2);display:flex;align-items:center;justify-content:center}
.service-card.featured .service-visual{background:var(--yellow)}
.service-visual i{width:130px;height:130px;border-radius:50%;background:radial-gradient(circle,#f5d468,#c4921d 70%,transparent 72%)}
.service-card h3{font-family:"Montserrat",sans-serif;font-size:13px;font-weight:700;margin:20px 0 10px;color:var(--brown)}
.service-card.featured h3{color:var(--yellow-dark)}
.service-card p{font-size:12px;line-height:18px;color:var(--muted);margin-bottom:18px;padding:0 8px}

/* video */
.video-band{height:260px;background:linear-gradient(180deg,#2b2b2b,#181818);text-align:center;padding-top:56px;color:var(--white)}
.video-band h2{font-family:"Open Sans",sans-serif;font-weight:400;font-size:22px;color:var(--yellow);margin-bottom:24px}
.video-band .play{display:block;margin:0 auto 12px;width:64px;height:64px}
.video-band span{display:block;font-size:16px}

/* footer */
.site-footer{height:280px;background:var(--dark);display:flex;padding:60px 48px 0;color:#bbb}
.footer-col{width:276px}
.footer-col h4{font-family:"Montserrat",sans-serif;font-size:16px;color:var(--yellow);margin-bottom:18px}
.footer-col li{list-style:none;font-size:13px;line-height:24px;display:flex;align-items:center;gap:10px}
.footer-col li::before{content:"";width:5px;height:5px;border-radius:50%;background:var(--yellow)}
.footer-col.contact li::before{display:none}
.footer-col.contact li.address{align-items:flex-start}
.footer-col.contact li.address svg{margin-top:5px}
.footer-col.contact svg{flex:none}

/* bottom bar */
.bottom-bar{height:84px;background:var(--darker);display:flex;align-items:center;justify-content:space-between;padding:0 48px;color:#999;font-size:12px}
.bottom-links{text-align:center;line-height:20px}
.bottom-links .copy{color:var(--yellow-dark)}
.social{display:flex;gap:10px}
.social i{width:26px;height:26px;border-radius:50%;background:#444;display:block}
</style>
</head>
<body>

<header class="site-header">
  <div class="brand"><span class="brand-dot"></span>Lindmark Schöfer</div>
  <div class="contact-bar">
    <span><span class="icon-round"><svg width="14" height="10" viewBox="0 0 14 10"><rect x="0.5" y="0.5" width="13" height="9" fill="none" stroke="#3b2417"/><path d="M0.5 0.5 L7 5.5 L13.5 0.5" fill="none" stroke="#3b2417"/></svg></span>info@lindmark-schoefer.de</span>
    <span><span class="icon-round"><svg width="12" height="14" viewBox="0 0 12 14"><path d="M2 1 L5 1 L6 4 L4 5.5 Q5.5 9 8 10 L9.5 8 L12 9.5 L11.5 13 Q3 13 1 3 Z" fill="#3b2417"/></svg></span>030 4471 2290</span>
  </div>
</header>

<nav class="main-nav">
  <a class="active">Startseite</a><a>Kollektion</a><a>Partnerringe</a><a>Brautschmuck</a><a>Informationen</a><a>Kontakt</a>
</nav>

<section class="hero">
  <div class="hero-visual" role="img" aria-label="Zwei goldene Eheringe ineinander verschlungen"></div>
  <div class="hero-text">
    <h1>Lorem ipsum dolor consectetur elit</h1>
    <p>Lorem ipsum dolor sit amet, consectetur adipiscing elit, sed do eiusmod tempor incididunt ut labore et dolore magna aliqua. Ut enim ad minim veniam, quis nostrud exercitation ullamco laboris nisi ut aliquip ex ea commodo consequat.</p>
    <a class="btn btn-yellow">Read more</a>
  </div>
  <div class="hero-dots"><i></i><i class="on"></i><i></i></div>
</section>

<section class="welcome">
  <h2 class="section-title"><span>Welcome to <em>Lindmark-Schöfer</em></span></h2>
  <p>Lorem ipsum dolor sit amet, consectetur adipiscing elit, sed do eiusmod tempor incididunt ut labore et dolore magna aliqua. Ut enim ad minim veniam, quis nostrud exercitation ullamco laboris nisi ut aliquip ex ea commodo consequat. Duis aute irure dolor in reprehenderit in voluptate velit esse cillum dolore eu fugiat nulla pariatur. Excepteur sint occaecat cupidatat non proident, sunt in culpa qui officia deserunt mollit anim id est laborum.</p>
  <a class="btn btn-brown">Read more</a>
</section>

<section class="feature">
  <div class="feature-text">
    <h2>Lorem Ipsum Dolor Sit Amet<br>Consectetur Adipiscing Elit,</h2>
    <p>Lorem ipsum dolor sit amet, consectetur adipiscing elit, sed do eiusmod tempor incididunt ut labore et dolore magna aliqua. Ut enim ad minim veniam, quis nostrud exercitation ullamco laboris nisi ut aliquip ex ea commodo consequat. Duis aute irure dolor in reprehenderit in voluptate velit esse cillum dolore eu fugiat nulla pariatur.</p>
    <a class="btn btn-brown">Read more</a>
  </div>
  <div class="feature-visual" role="img" aria-label="Frau mit Ring an der Hand, Porträtfoto"></div>
</section>

<section class="services">
  <h2 class="section-title"><span>Our <em>Service</em></span></h2>
  <div class="service-grid">
    <article class="service-card">
      <div class="service-visual" role="img" aria-label="Goldener Ring mit Steinbesatz"><i></i></div>
      <h3>LINDMARK SCHÖFER</h3>
      <p>Lorem ipsum dolor sit amet, consectetur adipiscing elit, sed do eiusmod tempor incididunt ut labore.</p>
      <a class="btn btn-brown">Read more</a>
    </article>
    <article class="service-card featured">
      <div class="service-visual" role="img" aria-label="Zwei goldene Eheringe"><i></i></div>
      <h3>EDITION 2</h3>
      <p>Lorem ipsum dolor sit amet, consectetur adipiscing elit, sed do eiusmod tempor incididunt ut labore.</p>
      <a class="btn btn-yellow">Read more</a>
    </article>
    <article class="service-card">
      <div class="service-visual" role="img" aria-label="Paar goldener Trauringe"><i></i></div>
      <h3>EDITION 1</h3>
      <p>Lorem ipsum dolor sit amet, consectetur adipiscing elit, sed do eiusmod tempor incididunt ut labore.</p>
      <a class="btn btn-brown">Read more</a>
    </article>
    <article class="service-card">
      <div class="service-visual" role="img" aria-label="Goldener Ring mit Blütenmotiv"><i></i></div>
      <h3>EXKLUSIV</h3>
      <p>Lorem ipsum dolor sit amet, consectetur adipiscing elit, sed do eiusmod tempor incididunt ut labore.</p>
      <a class="btn btn-brown">Read more</a>
    </article>
  </div>
</section>

<section class="video-band">
  <h2>Der Wunsch Eures Lebens: Neue Eheringe</h2>
  <svg class="play" viewBox="0 0 64 64"><circle cx="32" cy="32" r="29" fill="none" stroke="#fff" stroke-width="3"/><path d="M26 20 L45 32 L26 44 Z" fill="#fff"/></svg>
  <span>Watch Video</span>
</section>

<footer class="site-footer">
  <div class="footer-col"><h4>Service</h4><ul><li>Lindmark Schöfer</li><li>Edition 1</li><li>Edition 2</li><li>Exklusiv</li></ul></div>
  <div class="footer-col"><h4>Service</h4><ul><li>Verlobung</li><li>Antragsringe</li><li>Gold &amp; Platin</li><li>Gravur</li></ul></div>
  <div class="footer-col"><h4>Service</h4><ul><li>Beratung vor Ort</li><li>Ringgrößen messen</li><li>Werkstatt</li><li>Impressum</li></ul></div>
  <div class="footer-col contact"><h4>Contact Us</h4><ul>
    <li><svg width="12" height="14" viewBox="0 0 12 14"><path d="M2 1 L5 1 L6 4 L4 5.5 Q5.5 9 8 10 L9.5 8 L12 9.5 L11.5 13 Q3 13 1 3 Z" fill="#e9b503"/></svg>030 4471 2290</li>
    <li><svg width="12" height="14" viewBox="0 0 12 14"><path d="M2 1 L5 1 L6 4 L4 5.5 Q5.5 9 8 10 L9.5 8 L12 9.5 L11.5 13 Q3 13 1 3 Z" fill="#e9b503"/></svg>030 4471 2291</li>
    <li><svg width="14" height="10" viewBox="0 0 14 10"><rect x="0.5" y="0.5" width="13" height="9" fill="none" stroke="#e9b503"/><path d="M0.5 0.5 L7 5.5 L13.5 0.5" fill="none" stroke="#e9b503"/></svg>info@lindmark-schoefer.de</li>
    <li class="address"><svg width="12" height="14" viewBox="0 0 12 14"><path d="M6 0 A5 5 0 0 1 11 5 Q11 9 6 14 Q1 9 1 5 A5 5 0 0 1 6 0 Z" fill="#e9b503"/><circle cx="6" cy="5" r="2" fill="#1f1f1f"/></svg><span>Lindmark Schöfer<br>Ringstraße 12, 10115 Berlin</span></li>
  </ul></div>
</footer>

<div class="bottom-bar">
  <div class="brand" style="font-size:16px"><span class="brand-dot" style="width:20px;height:20px"></span>Lindmark Schöfer</div>
  <div class="bottom-links">
    <div>Home | Privacy | Terms &amp; Conditions | Impressum | Site Map</div>
    <div class="copy">Copyright © 2014 Lindmark Schöfer. All rights reserved.</div>
  </div>
  <div class="social" aria-label="Soziale Netzwerke"><i></i><i></i></div>
</div>

</body>
</html>
```